Business Card for Bright Meadow Lawn & Landscape

Double Sided Card Design - I think one side of the card should be cleaner, with logo, contact info, and "Complete Residential & Commercial Landscape Services", and on the other side it should list the services we offer:

- Lawn Care & Mowing
- Hedge & Shrub Trimming
- Leaf Removal & Clean Up
- Aeration & Sod
- Mulch & Rock Installations
- Landscape Installations & Renovations
- Commercial Snow Removal

Please make it clean and very professional... don't want it too be too busy, but want to tell them what we do.

Target Market(s)

Residential and Commercial

Industry/Entity Type

Landscape

Contact Information for Business Card

Fully Insured
Tom Berrigan
410-555-0198
Tberrigan07@mailbox-example.com

Requirements
Must have
• Double Sided, Cleaner on one side, more information and text on the other side.

```html
<!DOCTYPE html>
<html lang="en">
<head>
<meta charset="utf-8">
<title>Bright Meadow Lawn &amp; Landscape — Business Card</title>
<link rel="stylesheet" href="https://fonts.googleapis.com/css2?family=Cinzel:wght@600&family=Crimson+Text:wght@400;600&display=swap">
<style>
  :root {
    --bg: #2a2a2a;
    --card-white: #ffffff;
    --card-black: #050505;
    --green: #7cb53a;
    --ink: #151515;
    --light: #f4f4f4;
  }
  * { box-sizing: border-box; margin: 0; padding: 0; }
  html, body { width: 1200px; height: 880px; overflow: hidden; }
  body {
    background: var(--bg);
    display: flex;
    flex-direction: column;
    align-items: center;
    justify-content: center;
    gap: 30px;
    font-family: "Crimson Text", Georgia, serif;
  }
  .card {
    position: relative;
    width: 700px;
    height: 400px;
    border-radius: 22px;
    overflow: hidden;
    box-shadow: 0 10px 30px rgba(0,0,0,.45);
  }
  .card-front { background: var(--card-white); }
  .card-back { background: var(--card-black); }

  .brand {
    position: absolute;
    display: flex;
    align-items: center;
    gap: 16px;
  }
  .brand-mark {
    width: 62px; height: 62px;
    border-radius: 50%;
    border: 7px solid var(--green);
    flex: none;
  }
  .brand-name {
    font-family: "Cinzel", Georgia, serif;
    font-weight: 600;
    color: var(--green);
    font-size: 26px;
    line-height: 1.15;
    letter-spacing: .5px;
  }
  .card-front .brand { left: 50%; top: 120px; transform: translateX(-50%); }
  .tagline {
    position: absolute;
    left: 0; right: 0; top: 285px;
    text-align: center;
    font-size: 18px;
    color: var(--ink);
  }

  .back-shapes { position: absolute; inset: 0; }
  .card-back .brand { left: 468px; top: 150px; gap: 12px; }
  .card-back .brand-mark { width: 50px; height: 50px; border-width: 6px; }
  .card-back .brand-name { font-size: 21px; }

  .details {
    position: absolute;
    left: 62px; top: 42px;
    color: var(--light);
  }
  .person {
    font-family: "Cinzel", Georgia, serif;
    font-weight: 600;
    color: var(--green);
    font-size: 22px;
    letter-spacing: .5px;
  }
  .contact { list-style: none; margin-top: 10px; }
  .contact li {
    display: flex; align-items: center; gap: 9px;
    font-size: 16px; line-height: 24px;
  }
  .contact svg { width: 18px; height: 18px; flex: none; }
  .section-title {
    font-family: "Cinzel", Georgia, serif;
    font-weight: 600;
    color: var(--green);
    font-size: 19px;
    margin-top: 16px;
    letter-spacing: .4px;
  }
  .services { list-style: none; margin-top: 6px; margin-left: 4px; }
  .services li {
    position: relative;
    padding-left: 18px;
    font-size: 16px;
    line-height: 20px;
  }
  .services li::before {
    content: "";
    position: absolute; left: 0; top: 8px;
    width: 6px; height: 6px; border-radius: 50%;
    background: var(--green);
  }
  .insured {
    font-family: "Cinzel", Georgia, serif;
    font-weight: 600;
    color: var(--green);
    font-size: 17px;
    margin-top: 12px;
    letter-spacing: .4px;
  }
</style>
</head>
<body>

  <section class="card card-front">
    <div class="brand">
      <span class="brand-mark"></span>
      <span class="brand-name">Bright Meadow<br>Lawn &amp; Landscape</span>
    </div>
    <p class="tagline">Complete Residential &amp; Commercial Landscape Services</p>
  </section>

  <section class="card card-back">
    <svg class="back-shapes" viewBox="0 0 700 400" width="700" height="400" aria-hidden="true">
      <path d="M372 0 C405 170 480 320 600 400" fill="none" stroke="var(--green)" stroke-width="6"/>
      <path d="M380 0 L700 0 L700 400 L612 400 C492 322 414 172 380 0 Z" fill="var(--card-white)"/>
      <path d="M0 98 A24 24 0 0 1 0 146 Z" fill="var(--green)"/>
    </svg>

    <div class="brand">
      <span class="brand-mark"></span>
      <span class="brand-name">Bright Meadow<br>Lawn &amp; Landscape</span>
    </div>

    <div class="details">
      <p class="person">Tom Berrigan</p>
      <ul class="contact">
        <li>
          <svg viewBox="0 0 18 18"><circle cx="9" cy="9" r="8" fill="none" stroke="var(--green)" stroke-width="1.5"/><rect x="6.3" y="4.5" width="5.4" height="9" rx="1" fill="none" stroke="var(--green)" stroke-width="1.3"/></svg>
          410-555-0198
        </li>
        <li>
          <svg viewBox="0 0 18 18"><circle cx="9" cy="9" r="8" fill="none" stroke="var(--green)" stroke-width="1.5"/><rect x="5" y="6" width="8" height="6" fill="none" stroke="var(--green)" stroke-width="1.3"/><path d="M5 6 L9 9.5 L13 6" fill="none" stroke="var(--green)" stroke-width="1.3"/></svg>
          Tberrigan07@mailbox-example.com
        </li>
      </ul>
      <p class="section-title">Services We Offer</p>
      <ul class="services">
        <li>Lawn Care &amp; Mowing</li>
        <li>Hedge &amp; Shrub Trimming</li>
        <li>Leaf Removal &amp; Clean Up</li>
        <li>Aeration &amp; Sod</li>
        <li>Mulch &amp; Rock Installations</li>
        <li>Landscape Installations &amp; Renovations</li>
        <li>Commercial Snow Removal</li>
      </ul>
      <p class="insured">Fully Insured</p>
    </div>
  </section>

</body>
</html>
```